Security Company Needs a Website *

We need a website that gives our clients information about the services we provide, methods of contacting us and landing page to advertise on social media sites.

We need five landing pages titled Home, About Us, Services, Contact Us and a Landing Page that can be linked to Chatterloop advertising.

About Us - Should have a section for Core Values & Ethics, Our Vision, Our Mission and Partners.

Services - This page should show the different categories which include CCTV, Security Alarms, Access Control and Fire Protection.

CCTV Service Description:
Closed circuit television (CCTV) has long been implemented by businesses as a surveillance tool in areas that need monitoring. With digital CCTV cameras, multiple video cameras transmit signals through a set of monitors. The cameras provide thorough surveillance of the area.

With vast technological improvements over the last ten years, businesses with CCTV systems can use unique IP cameras and video analytics to monitor traffic flows, people-count, implement facial and number plate recognition. Useful information about customer behaviour and demographics can be discovered too. CCTV helps prevent crime in many industries and can assist with the improvement of industrial processes, safety on transport systems and traffic monitoring.

Security Alarms Service Description:
Alarms systems are electronic devices programmed to alert people to specific dangers and detect intrusions, fire or theft. Security alarms, systems and access control monitoring combine to create an integrated surveillance solution, tailored to your business’ unique requirements. Our surveillance and alarm monitoring services are ideal for perimeter protection from unwanted intruders or potential dangers.

Access Control Services:
An access control system allows for the free flow of authorised personnel while denying entry to unwanted visitors. With walk-in thieves and trespassers shut out, you dramatically reduce your exposure to crime while increasing the security of your employees, visitors, information and assets.

* Control when and who is entering your premises
* Protect employees, assets and information
* Secure an area or sector
* Observe movement
* Integrate with other security systems

Our range of access control systems can be seamlessly linked to other systems in our portfolio. These include Fire Detection Systems, Intruder Alarms, CCTV, and Building Management. A common request involves the need for a CCTV camera to pan around and focus on a door that has been highlighted as a security risk by the access control system.

Fire Protection Service:
To Be Advised

The above copy-writing will also have to be changed.

Contact Us - This form needs to be simple and straightforward to gather the prospects information and we would like to have a call to action on this page. The Contact Us page should also have a wayfindr charts location of our office address.

We would also like to have a link to our chatterloop page on the website.

Target Market(s)

Commercial businesses, building construction developers and property managers.

Industry/Entity Type

Security

Number of Pages Required

5+ page

Font styles to use
Sans Serif

Colors

Designer to choose colors to be used in the design.

Requirements
Must have
• We need to have the same look and feel as well as website features as the following website:
• https://www.kelvaguard.example.au/business-security/
• The website must be easy to use and easy to edit as well.

```html
<!DOCTYPE html>
<html lang="en">
<head>
<meta charset="utf-8">
<title>Halcyon Security</title>
<link href="https://fonts.googleapis.com/css2?family=Poppins:wght@300;400;500;600;700&display=swap" rel="stylesheet">
<style>
:root{
  --accent:#1ba8e0;
  --navy:#16245c;
  --ink:#333740;
  --muted:#6f737a;
  --line:#e3e5e8;
  --white:#ffffff;
  --footer:#5f6063;
  --sky-top:#1a63c9;
  --sky-bottom:#6fb2ee;
}
*{box-sizing:border-box;margin:0;padding:0}
html,body{width:1200px;height:3766px;overflow:hidden;background:var(--white)}
body{font-family:"Poppins",Arial,sans-serif;color:var(--ink);position:relative}
a{color:inherit;text-decoration:none}

/* header */
.site-header{position:absolute;left:0;top:0;width:1200px;height:128px;background:var(--white)}
.brand{position:absolute;left:160px;top:50px;display:flex;align-items:center;gap:8px}
.brand-mark{width:12px;height:12px;background:var(--navy);display:block}
.brand-name{font-size:15px;font-weight:600;color:var(--navy);line-height:1;white-space:nowrap}
.main-nav{position:absolute;left:346px;top:52px;display:flex;gap:34px;font-size:12px;font-weight:500;color:var(--ink);letter-spacing:.4px}
.main-nav .is-active{color:var(--accent)}
.header-phone{position:absolute;left:716px;top:50px;font-size:12px;color:var(--ink);display:flex;align-items:center;gap:8px}
.header-sep{position:absolute;left:856px;top:46px;width:1px;height:24px;background:var(--line)}
.header-search{position:absolute;left:870px;top:52px}
.btn-cta{position:absolute;left:896px;top:44px;width:144px;height:34px;border:3px solid var(--accent);border-radius:17px;font-size:11px;font-weight:600;display:flex;align-items:center;justify-content:center;color:var(--ink)}

/* hero */
.hero{position:absolute;left:0;top:128px;width:1200px;height:502px;background:linear-gradient(180deg,var(--sky-top),var(--sky-bottom))}
.hero-pole{position:absolute;left:660px;top:50px;width:230px;height:452px;background:linear-gradient(180deg,rgba(240,243,247,.35),rgba(60,70,85,.45));border-radius:4px}
.hero-kicker{position:absolute;left:160px;top:184px;font-size:12px;color:var(--white)}
.hero-title{position:absolute;left:158px;top:196px;font-size:48px;font-weight:300;color:var(--white)}
.hero-sub{position:absolute;left:160px;top:258px;font-size:11px;color:var(--white)}
.btn-hero{position:absolute;left:160px;top:302px;width:120px;height:30px;border:2px solid var(--accent);border-radius:15px;color:var(--white);font-size:11px;display:flex;align-items:center;justify-content:center}
.hero-arrow{position:absolute;top:236px;width:30px;height:30px;border:1px solid var(--white);border-radius:50%;display:flex;align-items:center;justify-content:center}
.hero-caption{position:absolute;left:868px;top:86px;border-left:2px solid var(--white);padding-left:10px;width:190px;font-size:10px;line-height:1.4}
.hero-caption strong{color:var(--white);font-weight:600;display:block}
.hero-caption span{color:#7fd3f7}

/* feature cards */
.features{position:absolute;left:160px;top:587px;width:880px;height:203px;background:var(--white);display:flex;padding:28px 20px 0}
.feature{width:210px;padding:0 15px;position:relative}
.feature h3{font-size:13px;font-weight:600;line-height:1.25;color:var(--ink);width:120px}
.feature p{font-size:10px;color:var(--muted);line-height:1.5;margin-top:14px;height:48px}
.feature .rule{height:1px;background:var(--line);margin-top:4px}
.feature.is-active .rule{height:2px;background:var(--accent)}
.feature .more{font-size:10px;margin-top:14px;color:var(--ink)}
.feature svg{position:absolute;right:18px;top:0}
.divider{position:absolute;left:160px;top:798px;width:880px;height:1px;background:var(--line)}

/* strip */
.strip-media{position:absolute;left:0;top:868px;width:200px;height:82px;background:linear-gradient(135deg,#dfe2e6,#8b9199)}
.strip-text{position:absolute;left:225px;top:862px;font-size:15px;color:var(--muted);font-weight:500}
.btn-outline{border:3px solid var(--accent);border-radius:17px;font-size:11px;font-weight:500;display:flex;align-items:center;justify-content:center;color:var(--ink)}
.strip-btn{position:absolute;left:833px;top:858px;width:142px;height:32px}

/* bands */
.band{position:absolute;left:0;width:1200px;text-align:center;color:var(--white)}
.band-navy{top:950px;height:420px;background:var(--navy)}
.band-mission{top:2251px;height:502px;background:linear-gradient(180deg,#8a8b8d,#6a6c70)}
.eyebrow{font-size:11px;color:var(--accent);font-weight:500}
.band h2{font-size:44px;font-weight:300;line-height:1.2;margin-top:6px}
.band p{width:580px;margin:14px auto 0;font-size:11.5px;line-height:1.65}
.band .btn-outline{width:142px;height:32px;margin:22px auto 0;color:var(--white)}
.band-mission .eyebrow{color:var(--white)}
.band-mission .btn-fill-white{width:142px;height:30px;margin:22px auto 0;border-radius:15px;background:var(--white);color:var(--ink);font-size:11px;display:flex;align-items:center;justify-content:center}
.mission-cam{position:absolute;left:130px;top:80px;width:140px;height:80px;background:linear-gradient(135deg,#5a5d62,#3c3e42);border-radius:6px;transform:rotate(18deg)}

/* services */
.section-head{position:absolute;left:0;top:1424px;width:1200px;text-align:center}
.section-head h2{font-size:44px;font-weight:300;color:var(--ink);line-height:1.2;margin-top:4px}
.service{position:absolute;left:213px;width:804px;height:263px}
.service-media{position:absolute;top:0;width:377px;height:263px}
.service-body{position:absolute;top:0;width:377px}
.service.media-left .service-media{left:0}
.service.media-left .service-body{left:427px}
.service.media-right .service-media{left:427px}
.service.media-right .service-body{left:0}
.service h3{font-size:22px;font-weight:300;color:var(--accent);border-left:3px solid var(--accent);padding-left:12px;line-height:1.15;margin-top:8px}
.service p{font-size:10.5px;color:var(--muted);line-height:1.65;margin-top:16px;width:360px}
.service p + p{margin-top:14px}
.btn-fill{width:100px;height:30px;border-radius:15px;background:var(--accent);color:var(--white);font-size:10.5px;display:flex;align-items:center;justify-content:center;margin-top:22px}
.btn-dark{width:100px;height:30px;border-radius:15px;border:3px solid var(--ink);color:var(--ink);font-size:10.5px;display:flex;align-items:center;justify-content:center;margin-top:22px}

/* footer */
.to-top{position:absolute;left:1104px;top:3489px;width:36px;height:36px;background:var(--navy);display:flex;align-items:center;justify-content:center}
.site-footer{position:absolute;left:0;top:3516px;width:1200px;height:250px;background:var(--footer);color:var(--white)}
.footer-brand{position:absolute;left:160px;top:100px;display:flex;align-items:center;gap:8px}
.footer-brand .brand-mark{background:var(--white)}
.footer-brand .brand-name{color:var(--white)}
.copyright{position:absolute;left:160px;top:170px;font-size:9px;line-height:1.5}
.footer-col{position:absolute;top:52px;font-size:9.5px;line-height:2.1}
.footer-col h4{font-size:11px;font-weight:600;letter-spacing:.5px;margin-bottom:8px;line-height:1}
.contact-line{display:flex;align-items:center;gap:6px}
.social{display:grid;grid-template-columns:repeat(3,22px);gap:14px 14px;margin-top:8px}
.social span{width:22px;height:22px;background:var(--white);border-radius:3px;display:block}
.social span.is-accent{background:var(--accent)}
.legal{position:absolute;left:900px;top:190px;font-size:9px}
</style>
</head>
<body>

<header class="site-header">
  <div class="brand">
    <span class="brand-mark"></span>
    <span class="brand-name">Halcyon Security</span>
  </div>
  <nav class="main-nav">
    <a class="is-active">HOME</a><a>ABOUT</a><a>SERVICES ⌄</a><a>CONTACT</a>
  </nav>
  <div class="header-phone">
    <svg width="14" height="14" viewBox="0 0 24 24"><path d="M6.6 10.8a15 15 0 0 0 6.6 6.6l2.2-2.2a1 1 0 0 1 1-.25 11.4 11.4 0 0 0 3.6.57 1 1 0 0 1 1 1V20a1 1 0 0 1-1 1A17 17 0 0 1 3 4a1 1 0 0 1 1-1h3.5a1 1 0 0 1 1 1c0 1.25.2 2.45.57 3.57a1 1 0 0 1-.25 1z" fill="none" stroke="#1ba8e0" stroke-width="1.8"/></svg>
    +44 4040 112233
  </div>
  <div class="header-sep"></div>
  <svg class="header-search" width="14" height="14" viewBox="0 0 24 24"><circle cx="10" cy="10" r="7" fill="none" stroke="#333740" stroke-width="2.4"/><path d="M15 15l6 6" stroke="#333740" stroke-width="2.4"/></svg>
  <a class="btn-cta">Secure your premises</a>
</header>

<section class="hero" role="img" aria-label="Sky with a pole of surveillance cameras">
  <div class="hero-pole"></div>
  <div class="hero-caption"><strong>Closed Circuit Television (CCTV)</strong><span>Unique IP cameras and video analytics to monitor</span></div>
  <div class="hero-kicker">Halcyon</div>
  <div class="hero-title">Security</div>
  <div class="hero-sub">Best surveillance tools</div>
  <a class="btn-hero">Learn More</a>
  <div class="hero-arrow" style="left:30px"><svg width="10" height="10" viewBox="0 0 10 10"><path d="M7 1L3 5l4 4" fill="none" stroke="#fff" stroke-width="1.5"/></svg></div>
  <div class="hero-arrow" style="left:1140px"><svg width="10" height="10" viewBox="0 0 10 10"><path d="M3 1l4 4-4 4" fill="none" stroke="#fff" stroke-width="1.5"/></svg></div>
</section>

<section class="features">
  <div class="feature">
    <h3>CCTV<br>System</h3>
    <svg width="34" height="26" viewBox="0 0 34 26"><rect x="2" y="4" width="24" height="9" rx="2" fill="#8a8e94"/><rect x="26" y="6" width="6" height="5" fill="#8a8e94"/><rect x="12" y="13" width="3" height="10" fill="#8a8e94"/></svg>
    <p>Implemented by businesses as a surveillance tool</p>
    <div class="rule"></div>
    <div class="more">Details ›</div>
  </div>
  <div class="feature is-active">
    <h3>Security<br>Alarms</h3>
    <svg width="30" height="28" viewBox="0 0 30 28"><path d="M7 22V14a8 8 0 0 1 16 0v8z" fill="#1ba8e0"/><rect x="4" y="22" width="22" height="4" fill="#1ba8e0"/><path d="M15 1v3M3 6l2 2M27 6l-2 2" stroke="#1ba8e0" stroke-width="2"/></svg>
    <p>Electronic devices to alert people to specific dangers.</p>
    <div class="rule"></div>
    <div class="more">Details ›</div>
  </div>
  <div class="feature">
    <h3>Access<br>Control</h3>
    <svg width="24" height="28" viewBox="0 0 24 28"><path d="M6 12V8a6 6 0 0 1 12 0v4" fill="none" stroke="#8a8e94" stroke-width="2.5"/><rect x="3" y="12" width="18" height="14" rx="2" fill="#8a8e94"/></svg>
    <p>Free flow of authorised personnel while denying entry.</p>
    <div class="rule"></div>
    <div class="more">Details ›</div>
  </div>
  <div class="feature">
    <h3>Fire<br>Protection</h3>
    <svg width="28" height="28" viewBox="0 0 28 28"><circle cx="14" cy="15" r="11" fill="none" stroke="#8a8e94" stroke-width="2.5"/><circle cx="14" cy="15" r="6" fill="#8a8e94"/></svg>
    <p>Seamlessly linked to include Fire Detection Systems.</p>
    <div class="rule"></div>
    <div class="more">Details ›</div>
  </div>
</section>
<div class="divider"></div>

<div class="strip-media" role="img" aria-label="Close view of a white security camera"></div>
<p class="strip-text">CCTV systems can use unique IP cameras and video analytics to monitor</p>
<a class="btn-outline strip-btn">How it works</a>

<section class="band band-navy">
  <div style="height:126px"></div>
  <div class="eyebrow">About Halcyon Solution</div>
  <h2>Core Values &amp; Ethics</h2>
  <p>Closed circuit television (CCTV) has long been implemented by businesses as a surveillance tool in areas that need monitoring. With digital CCTV cameras, multiple video cameras transmit signals through a set of monitors. The cameras provide thorough surveillance of the area.</p>
  <a class="btn-outline">Learn More</a>
</section>

<div class="section-head">
  <div class="eyebrow">Halcyon Solution</div>
  <h2>Services</h2>
</div>

<article class="service media-left" style="top:1556px">
  <div class="service-media" role="img" aria-label="Security camera mounted on a glass building facade" style="background:linear-gradient(135deg,#e9f0f6,#7e9bb5)"></div>
  <div class="service-body">
    <h3>Closed Circuit<br>Television</h3>
    <p>Closed circuit television (CCTV) has long been implemented by businesses as a surveillance tool in areas that need monitoring. With digital CCTV cameras, multiple video cameras transmit signals through a set of monitors. The cameras provide thorough surveillance of the area.</p>
    <p>With vast technological improvements over the last ten years, businesses with CCTV systems can use unique IP cameras</p>
    <a class="btn-fill">Details</a>
  </div>
</article>

<article class="service media-right" style="top:1908px">
  <div class="service-media" role="img" aria-label="Bright white office with desk and chair" style="background:linear-gradient(135deg,#f1f2f3,#b9bcc0)"></div>
  <div class="service-body">
    <h3>Security Alarms</h3>
    <p>Closed circuit television (CCTV) has long been implemented by businesses as a surveillance tool in areas that need monitoring. With digital CCTV cameras, multiple video cameras transmit signals through a set of monitors. The cameras provide thorough surveillance of the area.</p>
    <p>With vast technological improvements over the last ten years, businesses with CCTV systems can use unique IP cameras</p>
    <a class="btn-dark">Details</a>
  </div>
</article>

<section class="band band-mission" role="img" aria-label="Camera on a grey concrete wall">
  <div class="mission-cam"></div>
  <div style="height:162px"></div>
  <div class="eyebrow">About Halcyon Solution</div>
  <h2>Our Mission</h2>
  <p>Closed circuit television (CCTV) has long been implemented by businesses as a surveillance tool in areas that need monitoring. With digital CCTV cameras, multiple video cameras transmit signals through a set of monitors. The cameras provide thorough surveillance of the area.</p>
  <a class="btn-fill-white">Learn More</a>
</section>

<article class="service media-left" style="top:2829px">
  <div class="service-media" role="img" aria-label="Hand entering a code on an alarm keypad against red" style="background:linear-gradient(135deg,#e3343c,#f2f2f2 60%,#d92b33)"></div>
  <div class="service-body">
    <h3>Access Control</h3>
    <p>Closed circuit television (CCTV) has long been implemented by businesses as a surveillance tool in areas that need monitoring. With digital CCTV cameras, multiple video cameras transmit signals through a set of monitors. The cameras provide thorough surveillance of the area.</p>
    <p>With vast technological improvements over the last ten years, businesses with CCTV systems can use unique IP cameras</p>
    <a class="btn-fill">Details</a>
  </div>
</article>

<article class="service media-right" style="top:3175px">
  <div class="service-media" role="img" aria-label="Firefighter in protective gear with smoke and flames" style="background:linear-gradient(135deg,#2a2522,#c0632e 70%,#e69a55)"></div>
  <div class="service-body">
    <h3>Fire Protection</h3>
    <p>Closed circuit television (CCTV) has long been implemented by businesses as a surveillance tool in areas that need monitoring. With digital CCTV cameras, multiple video cameras transmit signals through a set of monitors. The cameras provide thorough surveillance of the area.</p>
    <p>With vast technological improvements over the last ten years, businesses with CCTV systems can use unique IP cameras</p>
    <a class="btn-dark">Details</a>
  </div>
</article>

<footer class="site-footer">
  <div class="footer-brand">
    <span class="brand-mark"></span>
    <span class="brand-name">Halcyon Security</span>
  </div>
  <div class="copyright">© 2018 Halcyon Solution<br>All Rights Reserved.</div>
  <div class="footer-col" style="left:398px">
    <h4>SITEMAP</h4>
    Home<br>About<br>Services<br>Contact
  </div>
  <div class="footer-col" style="left:543px">
    <h4>LOCATION</h4>
    <div style="line-height:1.5">North Dock Bld. 12, Harbour City<br>Republic of Design</div>
    <div class="contact-line"><svg width="11" height="11" viewBox="0 0 24 24"><path d="M6.6 10.8a15 15 0 0 0 6.6 6.6l2.2-2.2a1 1 0 0 1 1-.25 11.4 11.4 0 0 0 3.6.57 1 1 0 0 1 1 1V20a1 1 0 0 1-1 1A17 17 0 0 1 3 4a1 1 0 0 1 1-1h3.5a1 1 0 0 1 1 1c0 1.25.2 2.45.57 3.57a1 1 0 0 1-.25 1z" fill="#fff"/></svg>+44 4040 112233</div>
    <div class="contact-line"><svg width="12" height="10" viewBox="0 0 24 18"><rect x="1" y="1" width="22" height="16" fill="none" stroke="#fff" stroke-width="2"/><path d="M1 1l11 9 11-9" fill="none" stroke="#fff" stroke-width="2"/></svg>info@halcyonsec.example</div>
  </div>
  <div class="footer-col" style="left:900px">
    <h4>SOCIAL</h4>
    <div class="social">
      <span class="is-accent" title="Chatterloop"></span><span title="Social link"></span><span title="Social link"></span>
      <span title="Social link"></span><span title="Social link"></span>
    </div>
  </div>
  <div class="legal">Privacy | Legal | T&amp;C | Cookies</div>
</footer>
<a class="to-top"><svg width="12" height="8" viewBox="0 0 12 8"><path d="M1 7l5-5 5 5" fill="none" stroke="#fff" stroke-width="2"/></svg></a>

</body>
</html>
```